Company raising consciousness thru leadership & self-awareness needs amazing Letterhead

We are a technology company that spun out of a consulting firm. We are waking people up in corporate America through surveys, leadership development, workshops and consulting. Getting employees to become self-aware and changing company culture through improved leadership and team effectiveness. We need Word letterhead for our proposals, handouts, and worksheets that match our brand standard, is fresh, and communicates trust, credibility and professionalism.

Target Market(s)

Our target clients are other businesses, and executive leaders and C-suite leaders in those companies.

Font styles to use
Sans Serif

Requirements
Must have
• A Word template we can use for handouts, proposals, executive summary, project management documents, and letters. We need our logo. Please add page number and date on the footer. Must match the theme of our new website in look and feel to match the brand we are trying to promote. Use the colors from our brand standard document I submitted.

```html
<!DOCTYPE html>
<html lang="en">
<head>
<meta charset="utf-8">
<title>Veradin Letterhead</title>
<link href="https://fonts.googleapis.com/css2?family=Open+Sans:wght@400;600&family=Lato:wght@400;700&display=swap" rel="stylesheet">
<style>
  :root {
    --brand-purple: #7e3aa8;
    --brand-navy: #233a78;
    --ink: #4a4a4a;
    --ink-dark: #2f2f2f;
    --paper: #ffffff;
  }
  * { margin: 0; padding: 0; box-sizing: border-box; }
  html, body { width: 1040px; height: 1200px; overflow: hidden; background: var(--paper); }
  .letterhead {
    position: relative;
    width: 1040px;
    height: 1200px;
    background: var(--paper);
    font-family: "Open Sans", sans-serif;
    color: var(--ink);
  }
  .top-band {
    position: absolute; top: 0; left: 0; right: 0;
    height: 20px; background: var(--brand-purple);
  }
  .brand {
    position: absolute; top: 74px; left: 0; right: 0;
    display: flex; justify-content: center; align-items: center; gap: 12px;
  }
  .brand-dot { width: 30px; height: 30px; border-radius: 50%; background: var(--brand-navy); }
  .brand-name {
    font-family: "Open Sans", sans-serif; font-weight: 600;
    font-size: 24px; color: var(--brand-navy); letter-spacing: 0.5px;
  }
  .block { position: absolute; left: 98px; width: 840px; font-size: 15.5px; }
  .issue-date { top: 215px; }
  .recipient { top: 252px; line-height: 18px; }
  .salutation { top: 356px; }
  .body-copy { top: 406px; }
  .body-copy p {
    font-size: 16px; letter-spacing: 0.25px;
    line-height: 27px; text-align: justify; hyphens: auto;
    margin-bottom: 27px;
  }
  .closing { top: 813px; }
  .signatory-name { top: 889px; font-size: 20px; color: var(--ink-dark); }
  .signatory-title { top: 921px; font-size: 15.5px; }
  .footer-address {
    position: absolute; top: 1119px; left: 0; right: 0; text-align: center;
    font-family: "Lato", sans-serif; font-size: 19px; color: var(--ink-dark);
  }
  .footer-band {
    position: absolute; bottom: 0; left: 0; right: 0; height: 50px;
    background: var(--brand-navy); color: #fff;
    display: flex; align-items: center; justify-content: center;
    font-family: "Lato", sans-serif; font-size: 19px;
  }
  .footer-band b { font-weight: 700; }
</style>
</head>
<body>
<div class="letterhead">
  <div class="top-band"></div>
  <div class="brand">
    <span class="brand-dot"></span>
    <span class="brand-name">Veradin Leadership Group</span>
  </div>

  <div class="block issue-date">Issuing Date: May 5, 2018</div>
  <div class="block recipient">
    Name Of Employee Mr. XYZABC<br>
    Address of Employee<br>
    Address Line 2 etc..
  </div>
  <div class="block salutation">Dear Mr.XYZABC</div>

  <div class="block body-copy">
    <p>Lorem Ipsum has been the industry's standard dummy text ever since the 1500s, when an unknown printer took a galley of type and scrambled it to make a type specimen book. It has survived not only five centuries, but also the leap into electronic typesetting, remaining essentially unchanged. It was popularised in the 1960s with the release of Fontleaf sheets containing Lorem Ipsum passages, and more recently with desktop publishing software like Pagecraft Studio including versions of Lorem Ipsum.</p>
    <p>Lorem Ipsum is simply dummy text of the printing and typesetting industry. Lorem Ipsum has been the industry's standard dummy text ever since the 1500s, when an unknown printer took a galley of type and scrambled it to make a type specimen book.</p>
    <p>It has survived not only five centuries, but also the leap into electronic typesetting, remaining essentially unchanged. It was popularised in the 1960s with the release of Fontleaf sheets containing Lorem IpsumIpsum passages.</p>
  </div>

  <div class="block closing">Yours Sincerely</div>
  <div class="block signatory-name">Marcus Hale</div>
  <div class="block signatory-title">Managing Director</div>

  <div class="footer-address">18 Harbor Lane, Suite 210, Postcode 30917 Eastland</div>
  <div class="footer-band">
    <span><b>P:</b> 044-555 018 273 | <b>E:</b> hello@veradin.example | www.veradin.example</span>
  </div>
</div>
</body>
</html>
```